Business Card Re-Design

Consulting Company: To build a high performance organization, you need great leaders at all levels throughout your organization. The Cedar Path Talent Institute engages, inspires, and educates current and future leaders to step beyond the ordinary and deliver exceptional results. This new breed of leaders will motivate your staff to leave the safety of complacency behind and come together to build an extraordinary organization. The current trend has been to ask our people to do more with fewer resources. People have been stepping up to the challenge, but more is required to ensure success with a new work paradigm. We work with your management team to build a successful strategy that will make your organization more effective. CPTI then supports your management team by providing a comprehensive set of proven services to empower your entire organization to successfully execute new strategies.Let CPTI help you optimize your organization’s individual and team performance today!

Target Market(s)

Federal, State and Local Government / Non profit

Industry/Entity Type

Management Consulting

Contact Information for Business Card

CPTI, inc (Cedar Path Talent Institute) Optimizing Individual and Organizational Performance

Colors
fee18a
ec1f27
474747
fbf289

Requirements
Must have
• Professional and high quality feel

```html
<!DOCTYPE html>
<html lang="en">
<head>
<meta charset="utf-8">
<title>Cedar Path Talent Institute – Business Card</title>
<link href="https://fonts.googleapis.com/css2?family=Oswald:wght@500&family=Lato:wght@400;700&display=swap" rel="stylesheet">
<style>
  :root {
    --backdrop: #141414;
    --card-front: #f3f3f3;
    --card-back: #b6ad84;
    --gold-deep: #8a7f45;
    --gold: #a89d6a;
    --gold-light: #ddd3a0;
    --ink: #3a3a3a;
  }
  html, body {
    margin: 0;
    width: 1200px;
    height: 900px;
    overflow: hidden;
    background: var(--backdrop);
  }
  .stage {
    position: relative;
    width: 1200px;
    height: 900px;
  }
  .card {
    position: absolute;
    top: 185px;
    width: 301px;
    height: 489px;
    border-radius: 14px;
    box-sizing: border-box;
  }
  .card--front {
    left: 299px;
    background: var(--card-front);
  }
  .card--back {
    left: 646px;
    background: var(--card-back);
    display: flex;
    align-items: center;
    justify-content: center;
  }
  .wordmark {
    position: absolute;
    left: 68px;
    top: 42px;
    margin: 0;
    font-family: "Oswald", sans-serif;
    font-weight: 500;
    font-size: 30px;
    line-height: 1.05;
    letter-spacing: 0.5px;
    color: var(--gold);
    text-transform: uppercase;
  }
  .contact {
    position: absolute;
    left: 0;
    right: 0;
    top: 255px;
    text-align: center;
    font-family: "Lato", sans-serif;
    color: var(--ink);
  }
  .contact__name {
    margin: 0;
    font-weight: 700;
    font-size: 16px;
    letter-spacing: 0.3px;
    color: var(--gold);
    text-transform: uppercase;
  }
  .contact__role {
    margin: 1px 0 0;
    font-size: 13px;
  }
  .contact__lines {
    list-style: none;
    margin: 16px 0 0;
    padding: 0;
    font-size: 13px;
    line-height: 18px;
  }
  .contact__lines li {
    display: flex;
    justify-content: center;
    align-items: center;
    gap: 6px;
  }
  .contact__lines svg {
    width: 10px;
    height: 10px;
    fill: var(--gold);
  }
  .contact__address {
    margin: 12px 0 0;
    font-style: normal;
    font-size: 13px;
    line-height: 17px;
  }
  .monogram {
    margin: 0;
    font-family: "Oswald", sans-serif;
    font-weight: 500;
    font-size: 112px;
    line-height: 1;
    color: var(--gold-light);
    letter-spacing: -2px;
  }
</style>
</head>
<body>
<main class="stage">
  <section class="card card--front" aria-label="Card front">
    <p class="wordmark">Cedar Path<br>Talent<br>Institute</p>
    <div class="contact">
      <p class="contact__name">Daniel R. Hale</p>
      <p class="contact__role">President/CEO</p>
      <ul class="contact__lines">
        <li>
          <svg viewBox="0 0 10 10" aria-hidden="true"><path d="M2 0.5 L3.6 2.6 L2.8 3.8 C3.4 5 4.9 6.6 6.2 7.2 L7.4 6.4 L9.5 8 L8.4 9.5 C4.5 9.2 0.8 5.5 0.5 1.6 Z"/></svg>
          <span>410.555.0182</span>
        </li>
        <li>
          <svg viewBox="0 0 10 10" aria-hidden="true"><path d="M2.5 0.5 H7 L7.5 1 V3.5 H9 C9.5 3.5 9.5 4 9.5 4 V9.5 H0.5 V4 C0.5 3.5 1 3.5 1 3.5 H2.5 Z M3.5 1.5 V3.5 H6.5 V1.5 Z M2 5 V6 H8 V5 Z"/></svg>
          <span>410.555.0147</span>
        </li>
        <li>
          <svg viewBox="0 0 10 10" aria-hidden="true"><path d="M0.5 2 H9.5 V8.5 H0.5 Z M1.2 2.6 L5 5.6 L8.8 2.6 Z" fill-rule="evenodd"/></svg>
          <span>info@cedarpath.com</span>
        </li>
      </ul>
      <address class="contact__address">2460 Harbor Ridge Lane<br>Glenmoor, MD 20799</address>
    </div>
  </section>
  <section class="card card--back" aria-label="Card back">
    <p class="monogram">CPTI</p>
  </section>
</main>
</body>
</html>
```